Enlighted Feel-Good Wrapper Design for Cannabis Snack Bar: Vesso Bars.

We need a logo and wrapper for the first product in our line-up, Lark Crisp Clover! - Honey Salted Nuts and Dark Chocolate. Please highlight the name Clover Lark Crisp!, more than the name Vesso Bars or flavor of the bar. The package dimensions unfolded and unsealed are 6.5 inches x 5.25 inches. I have uploaded 3 photos of similar bar wrappers as an example of the wrapper type. The winning design will be awarded an extra amount for the Vesso Bars logo from Pixel Harbor.

It is a nut based snack bar similar to brands like Brisk, Tidal Nibble, Pomi, and Ferro Bars. The difference is that this bar will contain THC and/or CBD oils. It is designed for the Medical Marijuana market in California. I would like the bar to be more upscale in design as we are going after a demographic with a higher disposable income and will be in their 30's-60's. We would like the brand to be appealing to both men and women. We would like the wrapper/logo to have an air of enlightenment to it. We want people to feel like they will be at peace when they eat this bar. Please do not make the design flashy, or decorated with marijuana leaves. We do not want something cheesy. We uploaded pictures of the bar so you can see what they look like. The packaging has to be OPAQUE.

Please include all the following. If you don't know specific values, weights or ingredients please fill the space with any text that can be substituted.

Label Regulatory Requirements:

(1) The identity of the product in a text size reasonably related to the most prominent printed matter on the panel;
(2) The words “cannabis-infused” immediately above the identity of the product in bold type and a text size larger than the text size used for the identity of the product;
(3) The cannabis product symbol uploaded in this post. The symbol shall be no smaller in size than half (.5) inch by half (.5) inch and shall be printed legibly and conspicuously;
(4) The net weight or volume of the contents of the package;

1.4 oz (40g)

(5) The THC content and CBD content for the package in its entirety, expressed in milligrams per package;

40mg

(6) The THC content and CBD content per serving, expressed in milligrams per serving;

10mg

(b) The primary panel text must be in type size no less than 6 point font and be in relation to the size of the primary panel and container.

40408. Informational Panel Labeling Requirements.
(a) The label for a medical cannabis product shall include an informational panel that includes the following:
(1) The licensed manufacturer and its contact number or website address;

Vesso Bars, San Diego, CA (555)302-7194, www.vessobars.example

(2) The date of manufacture;
(3) Each of the following statements:
(A) “SCHEDULE I CONTROLLED SUBSTANCE.”
(B) “KEEP OUT OF REACH OF CHILDREN AND ANIMALS” in bold print.
(C) “FOR MEDICAL USE ONLY.”
(D) “IF PREGNANT OR BREASTFEEDING, CONSULT A PHYSICIAN PRIOR TO USE.”
(E) “THE INTOXICATING EFFECTS OF THIS PRODUCT MAY BE DELAYED BY UP TO TWO HOURS.”
(F) “THIS PRODUCT MAY IMPAIR THE ABILITY TO DRIVE OR OPERATE MACHINERY, PLEASE USE EXTREME CAUTION.”
(4) A list of all product ingredients in descending order of predominance by weight or volume;

NUT MIXTURE:
almonds, peanuts, walnuts, puffed rice, flaxseed

SYRUP:
honey, brown rice syrup, sea salt, vanilla

CHOCOLATE DRIZZLE:
dark chocolate, coconut oil

(5) If an edible product that contains an ingredient, flavoring, coloring, or an incidental additive that bears or contains a major food allergen, the word “contains,” followed by a list of the applicable major food allergens;

Contains tree nuts.

(6) If an edible product, the names of any artificial food colorings contained in the product;
(7) If an edible product, the amount, in grams, of sodium, sugar, carbohydrates, and total fat per serving;

Dark Chocolate Sea Salt: 193 calories, 12.5g fat, 95mg sodium, 18.9g carbs, 2.1g fiber, 14g sugars, 5.2g protein

(8) The lot number;
(9) Instructions for use, such as the method of consumption or application, and any preparation necessary prior to use;
(10) The product expiration date, “use by” date, or “best by” date; and
(11) The unique identifier.
(b) The informational panel text shall be in a type size of no less than 6 point font and in relation to the size of the primary panel and container, unless there is insufficient area on the container available to print all the required information in a type size of no less than 6 point font. In such a case, the label shall include the warning statements required by paragraph (3) in a type size of no less than 6 point font, and the product shall be accompanied by a supplemental labeling that includes all of the information required by this section. The text of the supplemental labeling shall be no less than 8 point font.

The label shall not contain any of the following:

(a) Claims that the manufactured cannabis or cannabis product was grown in a California county when the cannabis was not grown there.
(b) The name of a California county unless the cannabis was grown there.
(c) Content that is or designed to be attractive to individuals under the age of 21, including but not limited to:
(1) Cartoons;
(2) Any likeness to images, characters, or phrases that are popularly used to advertise to children; or
(3) Any imitation of candy packaging or labeling.
(d) False labeling information. Labeling is false if it is false or misleading in any particular.
(e) Claims of health benefits or other physical benefits.
Updates

Industry/Entity Type

Retail

Logo Text

Vesso Bars

Colors

Designer to choose colors to be used in the design.

Requirements
Must have
• I would like to have a logo/icon of an cute owl or icon of a small tree branch with leaves and nut hanging off or anything else that you think would be a good logo incorporated with the company name "Vesso Bars." I uploaded a logo of an owl logo that I like. Feel free to adjust and create something creative, please do not copy it.
• The wrapper needs to reflect an upscale, natural, farm fresh, whole food product. We are trying to build a high end line of products that appeal to health conscious women and men ages 30 - 60 years old.
• Please include text from Allergen warning in one of the uploaded photos.
• Please add - "Gluten free" to the label, "Non GMO" or "GMO Free" and "No Soy" or "Soy Free", and "Dairy Free" as either writing or as an icon of some sort.
Nice to have
• Please see posted photos of some wrappers of food products that I like for ideas. Some color suggestions to incorporate: Red, Yellow, Green, Orange simply because these colors have been proven appealing to the eye for food labels. You may use one or a few of these and can balance them out with other colors. Please do not use traditional colors associated with cannabis such as dark brown or deep green. Subdued, natural looking versions of these may be okay if they are balanced out with other colors or the rest of the bar. I would also like the wrapper to have some graphics that can illustrate what the bar actually looks like so that people know whats inside!
• The final design should communicate:
• Freshness
• Organic
• Healthy
• Modern
Should not have
• I do not want this product to have graphics of typical cheesy cannabis/marijuana leaves or any other low class graphics related to the industry. Not graphics of marijuana flower, joints, smoke or leaves.

```html
<!DOCTYPE html>
<html lang="en">
<head>
<meta charset="utf-8">
<title>Vesso Bars — Lark Crisp Clover! Wrapper</title>
<link rel="stylesheet" href="https://fonts.googleapis.com/css2?family=Oswald:wght@400;500;600;700&display=swap">
<style>
  :root {
    --stage: #ffffff;
    --cocoa: #3d2016;
    --cocoa-deep: #2a140c;
    --cocoa-sheen: #55301f;
    --crimp: #331a10;
    --amber: #f08a24;
    --cream: #ffffff;
  }
  * { box-sizing: border-box; margin: 0; padding: 0; }
  html, body {
    width: 1200px;
    height: 554px;
    overflow: hidden;
    background: var(--stage);
  }
  .canvas {
    position: relative;
    width: 1200px;
    height: 554px;
    font-family: "Oswald", sans-serif;
  }
  .wrapper-art {
    position: absolute;
    left: 0;
    top: 0;
  }
  .infused-label {
    position: absolute;
    left: 652px;
    top: 178px;
    font-weight: 700;
    font-size: 17px;
    line-height: 1;
    color: var(--cream);
    letter-spacing: 0.3px;
    white-space: nowrap;
  }
  .brand-name {
    position: absolute;
    left: 178px;
    top: 186px;
    font-weight: 700;
    font-size: 126px;
    line-height: 1;
    color: var(--cream);
    white-space: nowrap;
  }
  .tagline {
    position: absolute;
    left: 835px;
    top: 232px;
    width: 180px;
    font-weight: 700;
    font-size: 25px;
    line-height: 1.05;
    color: var(--amber);
    text-align: center;
    transform: rotate(-8deg);
    text-shadow:
      2px 0 0 var(--cream), -2px 0 0 var(--cream),
      0 2px 0 var(--cream), 0 -2px 0 var(--cream),
      2px 2px 0 var(--cream), -2px -2px 0 var(--cream),
      2px -2px 0 var(--cream), -2px 2px 0 var(--cream);
  }
  .product-line {
    position: absolute;
    left: 178px;
    top: 350px;
    display: flex;
    gap: 14px;
    font-size: 25px;
    line-height: 1.2;
    white-space: nowrap;
  }
  .flavour {
    font-weight: 500;
    color: var(--amber);
  }
  .net-weight {
    font-weight: 400;
    color: var(--cream);
  }
</style>
</head>
<body>
<main class="canvas" aria-label="Vesso Bars wrapper front panel">
  <svg class="wrapper-art" width="1200" height="554" viewBox="0 0 1200 554" xmlns="http://www.w3.org/2000/svg">
    <defs>
      <linearGradient id="wrapper-tone" x1="0" y1="0" x2="0" y2="1">
        <stop offset="0" stop-color="var(--cocoa-sheen)"/>
        <stop offset="0.3" stop-color="var(--cocoa)"/>
        <stop offset="0.75" stop-color="var(--cocoa)"/>
        <stop offset="1" stop-color="var(--cocoa-deep)"/>
      </linearGradient>
      <linearGradient id="bar-photo-tone" x1="0" y1="0" x2="1" y2="1">
        <stop offset="0" stop-color="#d9a86a"/>
        <stop offset="0.5" stop-color="#b9773b"/>
        <stop offset="1" stop-color="#e6c9a0"/>
      </linearGradient>
      <linearGradient id="nut-tone" x1="0" y1="0" x2="1" y2="0">
        <stop offset="0" stop-color="#c8894a"/>
        <stop offset="1" stop-color="#6b4428"/>
      </linearGradient>
      <clipPath id="wrapper-clip">
        <rect x="40" y="60" width="1120" height="440"/>
      </clipPath>
    </defs>
    <rect class="wrapper-body" x="40" y="60" width="1120" height="440" fill="url(#wrapper-tone)"/>
    <rect class="crimp-left" x="40" y="60" width="36" height="440" fill="var(--crimp)"/>
    <rect class="crimp-right" x="1124" y="60" width="36" height="440" fill="var(--crimp)"/>
    <g clip-path="url(#wrapper-clip)">
      <polygon class="accent-band" points="590,100 1124,100 1124,392" fill="var(--amber)"/>
      <g role="img" aria-label="Photo of the honey nut bar with dark chocolate drizzle">
        <polygon class="bar-photo" points="690,100 1124,100 1124,370" fill="url(#bar-photo-tone)"/>
      </g>
    </g>
    <g class="cannabis-symbol">
      <polygon points="815,160 882,160 848,222" fill="var(--amber)" stroke="var(--cream)" stroke-width="3" stroke-linejoin="round"/>
      <text x="848" y="184" text-anchor="middle" font-family="Oswald, sans-serif" font-weight="700" font-size="19" fill="var(--cream)">THC</text>
      <text x="848" y="197" text-anchor="middle" font-family="Oswald, sans-serif" font-weight="500" font-size="9" fill="var(--cream)">40mg</text>
    </g>
    <g role="img" aria-label="Illustration of almonds and a walnut">
      <ellipse class="nut-group" cx="910" cy="340" rx="110" ry="36" fill="url(#nut-tone)"/>
    </g>
  </svg>
  <div class="infused-label">CANNABIS-INFUSED</div>
  <div class="brand-name">Vesso Bars</div>
  <div class="tagline">Lark Crisp<br>Clover!</div>
  <div class="product-line">
    <span class="flavour">HONEY SALTED NUTS AND DARK CHOCOLATE</span>
    <span class="net-weight">1.4 OZ (40G)</span>
  </div>
</main>
</body>
</html>
```